Anzeigengestaltung Serviceblock
Sehr serviceorientiert, zügig und kreativ!
Zielgruppe
Wir sind eine klassische Steuerberatungsgesellschaft und richten uns vor allem an mittelständische Unternehmen und an das Handwerk. Zu finden sind wir unter www.fiskoralo.de.
Aufgabenstellung
Wir beabsichtigen eine regelmäßige monatliche Werbung mittels eines Serviceblocks in regionalen Zeitungen. Dazu wollen wir eine Art Rahmendesign, dass immer gleich aussieht, von uns aber mit wechselnden Info- Texten gefüllt werden kann. Das Design soll an das Design unserer Homepage angelehnt sein und unser Logo umfassen. Zudem sollen unsere Kontaktdaten gut zu ersehen sein. Muster solcher Serviceblöcke laden wir hoch - die sind aber nicht unbedingt unser Geschmack. Das Maß der Anzeige soll 325 mm breit und 163 mm hoch sein. Wir benötigen das Design als pdf, jpg und sonstiges zeitungskompatibles Format.

```html
<!DOCTYPE html>
<html lang="de">
<head>
<meta charset="utf-8">
<title>Fiskoralo – Serviceblock Kanzleiprofil</title>
<link rel="stylesheet" href="https://fonts.googleapis.com/css2?family=Open+Sans:wght@400;600;700&display=swap">
<style>
  :root {
    --teal: #147b86;
    --teal-glass: rgba(20, 123, 134, 0.88);
    --white: #ffffff;
    --paper: #eef0f1;
    --ink-logo: #4d6166;
    --photo-a: #7f9ba0;
    --photo-b: #3f5e73;
    --photo-c: #8a7458;
    --photo-d: #4a3b2f;
  }
  * { box-sizing: border-box; margin: 0; padding: 0; }
  html, body {
    width: 1071px; height: 1200px; overflow: hidden;
    background: var(--paper);
    font-family: "Open Sans", sans-serif;
  }
  .ad {
    position: absolute; left: 20px; top: 341px;
    width: 1031px; height: 518px;
    overflow: hidden; background: var(--photo-a);
  }
  .ad__photo {
    position: absolute; inset: 0;
    background:
      radial-gradient(ellipse 22% 35% at 58% 55%, var(--photo-b), transparent 70%),
      linear-gradient(160deg, var(--photo-a) 0%, #9aa9a8 40%, var(--photo-c) 70%, var(--photo-d) 100%);
  }
  .profile {
    position: absolute; left: 0; top: 0; width: 600px; height: 388px;
    background: linear-gradient(90deg, var(--teal-glass) 0%, rgba(20,123,134,0.82) 75%, rgba(20,123,134,0) 100%);
    padding: 32px 40px 0 38px; color: var(--white);
  }
  .profile__title { font-weight: 700; font-size: 32px; line-height: 1.1; }
  .rule { display: block; width: 42px; height: 3px; background: var(--white); margin: 12px 0 16px; }
  .profile__text { font-size: 12.6px; line-height: 1.45; margin-bottom: 10px; max-width: 500px; }
  .logo-box {
    position: absolute; left: 0; top: 388px; width: 310px; height: 100px;
    background: var(--white); display: flex; align-items: center; justify-content: center;
  }
  .logo {
    border: 1.5px solid var(--ink-logo); padding: 10px 20px;
    display: flex; align-items: center; gap: 12px; color: var(--ink-logo);
  }
  .logo__dot { width: 30px; height: 30px; border-radius: 50%; background: var(--ink-logo); }
  .logo__name { font-weight: 600; font-size: 26px; letter-spacing: 1px; line-height: 1; display: block; }
  .logo__sub { font-weight: 600; font-size: 9px; display: block; letter-spacing: 0.3px; margin-top: 3px; }
  .services {
    position: absolute; left: 712px; top: 116px; width: 250px; height: 284px;
    background: var(--teal-glass); color: var(--white); padding: 22px 18px 0 26px;
  }
  .services__title { font-weight: 700; font-size: 23px; line-height: 1.2; }
  .services .rule { width: 28px; margin: 10px 0 12px; }
  .services__list { list-style: none; font-size: 12.8px; line-height: 1.32; }
  .services__list li { padding-left: 10px; text-indent: -10px; }
  .services__list li::before { content: "• "; }
  .footer-band {
    position: absolute; left: 310px; top: 410px; width: 402px; height: 108px;
    background: var(--teal); color: var(--white);
    padding: 14px 20px; font-size: 12.8px; line-height: 1.5;
  }
  .contact-phone {
    position: absolute; left: 712px; top: 404px; width: 319px; height: 52px;
    background: var(--white); color: var(--teal);
    display: flex; align-items: center; gap: 14px; padding-left: 38px;
    font-weight: 700; font-size: 25px;
  }
  .contact-web {
    position: absolute; left: 712px; top: 456px; width: 319px; height: 62px;
    background: var(--teal); color: var(--white);
    display: flex; align-items: center; padding-left: 52px;
    font-weight: 700; font-size: 19px; letter-spacing: 0.5px;
  }
  .phone-icon { width: 26px; height: 26px; }
</style>
</head>
<body>
<section class="ad">
  <div class="ad__photo" role="img" aria-label="Foto: Frau in Jeanshemd arbeitet an einem Laptop an einem Holztisch"></div>

  <div class="profile">
    <h1 class="profile__title">Kanzleiprofil</h1>
    <span class="rule"></span>
    <p class="profile__text">Als Steuerberater beginnt unsere Beratung bei FISKORALO damit, genau zuzuhören. Denn es geht um Ihre ganz persönlichen Angelegenheiten. Nachfragen. Analysieren. Erst dann schlagen wir Ihnen passende Lösungen vor und begleiten Sie vertrauensvoll und verlässlich bei der Umsetzung.</p>
    <p class="profile__text">Wir verfügen als Steuerprofis über eine langjährige Erfahrung in der steuerlichen Beratung und Begleitung unserer Mandanten. Die dauerhafte Treue unserer zufriedenen Mandanten spricht hierbei für sich. FISKORALO steht Ihnen bei allen Fragen rund um das Thema Steuern unbürokratisch und lösungsorientiert zur Seite.</p>
    <p class="profile__text">Konzentrieren Sie sich auf Ihr Kerngeschäft – wir finden eine effiziente Entlastung für Ihren Alltag und sorgen für den richtigen Überblick, arbeiten Vergangenes auf und unterstützen Sie bei Ihren Entscheidungen für die Zukunft.</p>
  </div>

  <div class="logo-box">
    <div class="logo">
      <span class="logo__dot"></span>
      <div>
        <span class="logo__name">FISKORALO</span>
        <span class="logo__sub">Steuerberatungsgesellschaft mbH</span>
      </div>
    </div>
  </div>

  <aside class="services">
    <h2 class="services__title">Unsere<br>Leistungen</h2>
    <span class="rule"></span>
    <ul class="services__list">
      <li>Steuerberatung</li>
      <li>Unternehmensberatung</li>
      <li>Finanzbuchhaltung</li>
      <li>Lohnbuchhaltung</li>
      <li>Bilanzierung/ Steuererklärungen</li>
      <li>Existenzgründung</li>
      <li>Energiesteuerrecht</li>
      <li>Sanierungsberatung und Insolvenzsteuerrecht</li>
    </ul>
  </aside>

  <div class="footer-band">
    <strong>FISKORALO</strong> betreut überwiegend klein- und mittelständische Unternehmen, Freie Berufe und Privatpersonen in allen Bereichen der Steuerberatung und betriebswirtschaftlichen Beratung.
  </div>

  <div class="contact-phone">
    <svg class="phone-icon" viewBox="0 0 24 24" aria-hidden="true">
      <path fill="currentColor" d="M6.6 10.8a15.1 15.1 0 0 0 6.6 6.6l2.2-2.2a1 1 0 0 1 1-.25 11.4 11.4 0 0 0 3.6.57 1 1 0 0 1 1 1V20a1 1 0 0 1-1 1A17 17 0 0 1 3 4a1 1 0 0 1 1-1h3.5a1 1 0 0 1 1 1c0 1.25.2 2.45.57 3.57a1 1 0 0 1-.25 1z"/>
      <path fill="none" stroke="currentColor" stroke-width="1.6" stroke-linecap="round" d="M15 3.5a6 6 0 0 1 5.5 5.5M15 7a2.6 2.6 0 0 1 2.2 2.2"/>
    </svg>
    <span>02605 4418302</span>
  </div>
  <div class="contact-web">www.fiskoralo.de</div>
</section>
</body>
</html>
```